8.5 x 8.5 - HELOC Product Campaign

Home Equity Lines of Credit
are BACK!!!

* Up to 97.5% on Owner Occupied Properties
* 700 Minimum Scores
* Fund in only 2-3 weeks

Can be used for...
* Education Expense
* Bill Consolidation
* Home Improvement
* Investments

Call today for more information!
(800) 417-2960

Bluegate Lending Partners, Inc.
NMLS #381760
www.bluegatelendhub.com

```html
<!DOCTYPE html>
<html lang="en">
<head>
<meta charset="utf-8">
<title>HELOC Campaign – Bluegate Lending Partners</title>
<link rel="stylesheet" href="https://fonts.googleapis.com/css2?family=Bebas+Neue&family=Lato:wght@400;700;900&family=Playball&display=swap">
<style>
  :root{
    --backdrop:#b6b4c6;
    --olive:#958a25;
    --blue:#1a5ea6;
    --navy:#1c4f8f;
    --gold:#a89528;
    --white:#ffffff;
    --photo-light:#ece6df;
    --photo-mid:#cdb9a6;
    --photo-dark:#8a7565;
  }
  *{margin:0;padding:0;box-sizing:border-box}
  html,body{width:1200px;height:1200px;overflow:hidden}
  body{background:var(--backdrop);position:relative;font-family:"Lato",sans-serif}
  .flyer{position:absolute;left:131px;top:124px;width:942px;height:942px;background:var(--white);overflow:hidden}
  .side-panel{position:absolute;left:0;top:0;width:404px;height:814px;background:var(--olive)}
  .headline-band{position:absolute;left:314px;top:119px;width:628px;height:165px;background:var(--blue)}
  .photo-area{position:absolute;left:404px;top:284px;width:538px;height:530px;
    background:linear-gradient(160deg,var(--photo-light) 0%,var(--photo-mid) 60%,var(--photo-dark) 100%)}
  .house-mark{position:absolute;left:45px;top:18px;width:300px;height:296px}
  .house-title{position:absolute;left:74px;top:138px;width:240px;text-align:center;
    font-family:"Bebas Neue",sans-serif;color:var(--white);font-size:78px;line-height:66px}
  .call-prompt{position:absolute;right:23px;top:20px;color:var(--navy);font-weight:700;font-size:23px}
  .phone{position:absolute;right:67px;top:44px;color:var(--gold);font-weight:700;font-size:43px;letter-spacing:.5px}
  .band-title{position:absolute;left:368px;top:132px;font-family:"Bebas Neue",sans-serif;color:var(--white);font-size:78px;line-height:1}
  .band-script{position:absolute;right:45px;top:196px;font-family:"Playball",cursive;color:var(--white);font-size:72px;line-height:1}
  .features{position:absolute;left:42px;top:345px;list-style:none;color:var(--white);font-size:23px;line-height:33px}
  .features li{position:relative;padding-left:17px}
  .features li::before{content:"";position:absolute;left:0;top:10px;border-left:9px solid var(--white);border-top:6px solid transparent;border-bottom:6px solid transparent}
  .uses-pill{position:absolute;left:0;top:501px;width:364px;height:57px;background:var(--blue);border:2px solid var(--white);border-left:none;border-radius:0 29px 29px 0;
    color:var(--white);font-size:26px;font-weight:700;line-height:53px;padding-left:55px}
  .uses{position:absolute;left:24px;top:580px;list-style:none}
  .uses li{display:flex;align-items:center;height:55.5px;color:var(--white);font-weight:700;font-size:24px}
  .uses svg{width:52px;height:44px;margin-right:26px;flex:none}
  .footer-name-mark{position:absolute;left:108px;top:850px;display:flex;align-items:center;gap:10px;color:var(--navy);font-weight:700;font-size:17px;width:180px;line-height:1.15}
  .footer-name-mark .dot{width:26px;height:26px;border-radius:50%;background:var(--gold);flex:none}
  .company{position:absolute;left:402px;top:832px;font-size:34px;font-weight:700;color:var(--navy)}
  .company .accent{color:var(--gold)}
  .license{position:absolute;left:402px;top:870px;font-size:23px;font-weight:700;color:var(--navy)}
  .site{position:absolute;left:376px;top:898px;font-size:23px;font-weight:700;color:var(--navy);display:flex;align-items:center;gap:6px}
</style>
</head>
<body>
<main class="flyer">
  <div class="side-panel"></div>
  <div class="headline-band"></div>
  <div class="photo-area" role="img" aria-label="Photo of a smiling couple on a sofa looking at a tablet among moving boxes"></div>

  <svg class="house-mark" viewBox="0 0 300 296" aria-hidden="true">
    <path d="M12 126 L148 8 L290 126" fill="none" stroke="#fff" stroke-width="20" stroke-linejoin="miter"/>
    <path d="M42 110 V262 a24 24 0 0 0 24 24 H250 a24 24 0 0 0 24 -24 V110" fill="none" stroke="#fff" stroke-width="22"/>
  </svg>
  <h1 class="house-title">Home<br>Equity</h1>

  <p class="call-prompt">Call today for more information!</p>
  <p class="phone">(800) 417-2960</p>

  <h2 class="band-title">Lines of Credit</h2>
  <p class="band-script">are BACK!</p>

  <ul class="features">
    <li>Up to 97.5% on Owner<br>Occupied Properties</li>
    <li>700 Minimum Scores</li>
    <li>Fund in only 2-3 weeks</li>
  </ul>

  <p class="uses-pill">CAN BE USED FOR:</p>
  <ul class="uses">
    <li><svg viewBox="0 0 52 44" fill="none" stroke="#fff" stroke-width="3"><path d="M4 6h18v30H4zM26 6h18v30H26zM8 13h10M8 19h10M8 25h10M30 13h10M30 19h10"/><circle cx="42" cy="36" r="7"/></svg>EDUCATION EXPENSE</li>
    <li><svg viewBox="0 0 52 44" fill="none" stroke="#fff" stroke-width="3"><path d="M12 3h22v38H12zM17 12h12M17 20h12M17 28h12M17 35h8"/></svg>BILL CONSOLIDATION</li>
    <li><svg viewBox="0 0 52 44" fill="none" stroke="#fff" stroke-width="3"><path d="M6 22 L26 4 L46 22M12 17v24h28V17M21 41V29h10v12"/></svg>HOME IMPROVEMENT</li>
    <li><svg viewBox="0 0 52 44" fill="none" stroke="#fff" stroke-width="3"><circle cx="26" cy="13" r="11"/><path d="M26 24v18M26 36c-5-6-12-6-14-4M26 36c5-6 12-6 14-4"/><text x="26" y="18" text-anchor="middle" font-size="14" fill="#fff" stroke="none" font-family="Lato,sans-serif" font-weight="700">$</text></svg>INVESTMENTS</li>
  </ul>

  <div class="footer-name-mark"><span class="dot"></span><span>Bluegate Lending Partners, Inc.</span></div>
  <p class="company"><span class="accent">Bluegate</span> Lending Partners, Inc.</p>
  <p class="license">NMLS #381760</p>
  <p class="site"><svg width="20" height="20" viewBox="0 0 20 20" fill="none" stroke="#a89528" stroke-width="2"><circle cx="10" cy="10" r="8"/><path d="M2 10h16M10 2c4 4 4 12 0 16M10 2c-4 4-4 12 0 16"/></svg>www.bluegatelendhub.com</p>
</main>
</body>
</html>
```